Business Card design for an International Import Export House

We need a Business Card design for our import export business. We trade in Minerals, Metals, Rice, Sugar, Steel etc.. The design should be minimalistic. It may or may not contain the physical address. In case you want to include the physical address - 418 Verandah Heights, Marlow Sector 9, Dunmere, Halvani, India, 402716.

Target Market(s)

Steel Mills or Steel Plants, Factories, Mining businesses, Industrial houses, Government Agencies

Industry/Entity Type

Importer

Contact Information for Business Card

Business Name - Tessan Overseas

Font styles to use
Other font styles liked:
• montserrat

Requirements
Must have
• Ravi Kandola - President
• www.tessanoverseas.com
• ravi@tessanoverseas.com
• +91-987-654-3217
Nice to have
• worldwide suppliers of ores

```html
<!DOCTYPE html>
<html lang="en">
<head>
<meta charset="utf-8">
<title>Tessan Overseas – Business Card</title>
<link rel="stylesheet" href="https://fonts.googleapis.com/css2?family=Montserrat:wght@700&family=PT+Sans:wght@400;700&display=swap">
<style>
  :root {
    --backdrop-top: #2b2b2b;
    --backdrop-bottom: #050505;
    --card-white: #f3f3f3;
    --brand-teal: #2f7f98;
    --ink: #1c1c1c;
    --teal-light: #4aa6bd;
    --teal-deep: #347f98;
    --text-light: #ffffff;
  }
  * { margin: 0; padding: 0; box-sizing: border-box; }
  html, body { width: 1200px; height: 900px; overflow: hidden; }
  body {
    position: relative;
    background: linear-gradient(to bottom, var(--backdrop-top), var(--backdrop-bottom));
    font-family: "PT Sans", sans-serif;
  }
  .card {
    position: absolute;
    top: 184px;
    width: 302px;
    height: 490px;
    border-radius: 12px;
    box-shadow: 0 4px 14px rgba(0,0,0,0.5);
    overflow: hidden;
  }
  .card--front { left: 299px; background: var(--card-white); text-align: center; color: var(--ink); }
  .card--back  { left: 646px; width: 304px; }

  .brand-mark {
    position: absolute; left: 0; right: 0; top: 60px;
    display: flex; flex-direction: column; align-items: center; gap: 46px;
  }
  .brand-mark__dot { width: 76px; height: 76px; }
  .brand-mark__name {
    font-family: "Montserrat", sans-serif; font-weight: 700;
    font-size: 20px; letter-spacing: -0.3px; color: var(--brand-teal);
  }

  .holder { position: absolute; left: 0; right: 0; top: 251px; }
  .holder__name { font-size: 17px; font-weight: 700; line-height: 22px; }
  .holder__role { font-size: 13px; line-height: 16px; }
  .accent { color: var(--brand-teal); }

  .contact { position: absolute; left: 0; right: 0; top: 310px; font-size: 13px; line-height: 18px; }

  .office { position: absolute; left: 0; right: 0; top: 391px; font-size: 13px; line-height: 18.5px; }
  .office__company { font-size: 15px; font-weight: 700; }

  .back-art {
    position: absolute; inset: 0;
    background: linear-gradient(to bottom, var(--teal-light), var(--teal-deep));
  }
  .tagline {
    position: absolute; left: 0; right: 0; top: 231px;
    text-align: center; color: var(--text-light);
    font-size: 32px; line-height: 52px; letter-spacing: 0.4px;
    text-transform: uppercase;
  }
</style>
</head>
<body>
  <section class="card card--front">
    <div class="brand-mark">
      <svg class="brand-mark__dot" viewBox="0 0 76 76" aria-hidden="true">
        <circle cx="38" cy="38" r="36" fill="var(--brand-teal)"/>
      </svg>
      <div class="brand-mark__name">TESSAN OVERSEAS</div>
    </div>

    <div class="holder">
      <div class="holder__name"><span class="accent">Ravi</span> Kandola</div>
      <div class="holder__role">President</div>
    </div>

    <div class="contact">
      <div>+91-987-654-3217</div>
      <div>ravi@tessanoverseas.com</div>
      <div>www.<span class="accent">tessanoverseas</span>.com</div>
    </div>

    <div class="office">
      <div class="office__company"><span class="accent">TESSAN</span> OVERSEAS</div>
      <div>418 Verandah Heights, Marlow Sector 9,</div>
      <div>Dunmere, Halvani, India, 402716.</div>
    </div>
  </section>

  <section class="card card--back">
    <div class="back-art" role="img" aria-label="Faint dotted world map over a teal background"></div>
    <div class="tagline">
      Worldwide<br>Suppliers<br>Of<br>Ores
    </div>
  </section>
</body>
</html>
```